$15 per single page resume WEBSITE - Submit a quality responsive resume website and I might buy it

NO TEMPLATES

I'm interested in single page resume websites. Only HTML and CSS skills required. Must be browser friendly and mobile responsive. MUST MATCH THE QUALITY AS PROVIDED IN SCREENSHOT. NO DEVIATIONS. Any professional picture can be used for the picture in the resume. HTML & CSS files required during handover to complete project.

Resume design should be a maximum width of 1000px, vertical bars should be no wider than 300px. Quality work may result in additional projects. I anticipate that I may need 50 total resumes.

This project has a maximum budget of $15 per single page site being I have a large amount of work to be done. Please upload a resume to a server so that I can review it. If its quality work, not a template, and mobile responsive I might buy it. Once again I may need up to 50 different designs.

*** Many freelancers say they can do the work but few actually deliver quality. I can increase the per cost amount for a good employee that can deliver quality without frequent instruction. If you want to work with someone that may be able to provide you with lots of work, message me.

THE FLOW OF MOBILE ELEMENTS SHOULD BE FROM TOP TO BOTTOM:
PHOTO
CONTACT INFORMATION
OBJECTIVE
*EXPERIENCE OR SKILLS
* (Sometimes these need to be switched around based on the way the page looks)
*EXPERIENCE OR SKILLS
EDUCATION
INTERESTS/HOBBIES

Thank you
RV

```html
<!DOCTYPE html>
<html lang="en">
<head>
<meta charset="utf-8">
<title>Mara Quill — Resume</title>
<link rel="stylesheet" href="https://fonts.googleapis.com/css2?family=Arimo:wght@400;700&family=Open+Sans:wght@400;600&family=Raleway:ital,wght@1,700&display=swap">
<style>
  :root {
    --page-bg: #ffffff;
    --sheet-bg: #f0f0f0;
    --header-bg: #e6e6e6;
    --ink: #2a2a2a;
    --body-ink: #3a3a3a;
    --accent: #4a90e2;
    --bar-fill: #5ab0ea;
    --bar-track: #c9c9c9;
    --photo-a: #a48a78;
    --photo-b: #5f5148;
  }
  * { margin: 0; padding: 0; box-sizing: border-box; }
  html, body { width: 1200px; height: 767px; overflow: hidden; background: var(--page-bg); }
  body { font-family: "Arimo", Arial, sans-serif; color: var(--body-ink); }

  .resume {
    position: absolute; left: 287px; top: 0;
    width: 626px; height: 767px;
    background: var(--sheet-bg);
  }
  .resume-header {
    position: absolute; left: 0; top: 0; width: 100%; height: 100px;
    background: var(--header-bg);
    border-bottom: 1.5px dashed var(--accent);
  }
  .profile-photo { position: absolute; left: 13px; top: 13px; width: 75px; height: 75px; }
  .profile-name {
    position: absolute; left: 100px; top: 18px;
    font-family: "Open Sans", sans-serif; font-weight: 600;
    font-size: 31px; line-height: 1; color: var(--ink);
  }
  .profile-role {
    position: absolute; left: 101px; top: 55px;
    font-family: "Open Sans", sans-serif; font-size: 13px; color: var(--ink);
  }
  .contact {
    position: absolute; left: 437px; top: 16px; width: 180px;
    font-family: "Open Sans", sans-serif; font-weight: 600;
    font-size: 10px; line-height: 13px; color: var(--ink);
    font-style: normal;
  }

  .section-title {
    position: absolute; left: 20px;
    font-family: "Raleway", sans-serif; font-style: italic; font-weight: 700;
    font-size: 16px; color: var(--ink);
  }
  .section-label-plain {
    position: absolute; left: 0;
    font-family: "Arimo", sans-serif; font-size: 10.5px; color: var(--ink);
  }
  .section-body { position: absolute; left: 188px; width: 412px; }
  .text { font-size: 10.6px; line-height: 14.6px; }

  .entry-title {
    font-family: "Open Sans", sans-serif; font-weight: 600;
    font-size: 12.5px; line-height: 16px; color: var(--ink);
  }
  .entry-dates { font-size: 7px; color: var(--accent); margin-bottom: 11px; margin-top: 1px; }
  .entry + .entry { margin-top: 14px; }
  .entry-list { list-style: disc; padding-left: 24px; font-size: 9.5px; line-height: 13px; }
  .entry-list.tight { padding-left: 13px; }

  .skills { display: grid; grid-template-columns: 190px 190px; column-gap: 38px; row-gap: 9px; }
  .skill-name { font-size: 9px; line-height: 10px; color: var(--ink); }
  .skill-bar { height: 3px; background: var(--bar-track); margin-top: 3px; }
  .skill-level { height: 100%; background: var(--bar-fill); }

  .interests { font-size: 9px; color: var(--body-ink); }
</style>
</head>
<body>
<main class="resume">
  <header class="resume-header">
    <svg class="profile-photo" viewBox="0 0 75 75" role="img" aria-label="Professional portrait photo of the candidate">
      <defs>
        <radialGradient id="photoTone" cx="50%" cy="40%" r="60%">
          <stop offset="0%" stop-color="var(--photo-a)"/>
          <stop offset="100%" stop-color="var(--photo-b)"/>
        </radialGradient>
      </defs>
      <circle cx="37.5" cy="37.5" r="37.5" fill="url(#photoTone)"/>
    </svg>
    <h1 class="profile-name">Mara Quill</h1>
    <p class="profile-role">Graphic Design</p>
    <address class="contact">
      1288 Orlen Street, Fairhaven 3052,<br>United States<br>hello@quillmail.com<br>(555)204-7719
    </address>
  </header>

  <h2 class="section-title" style="top:128px">Objective</h2>
  <div class="section-body" style="top:131px">
    <p class="text">Lorem ipsum dolor sit amet, consectetur adipisicing elit. Inventore neque sint beatae cum explicabo laborum molestiae, minima, rerum illum eaque deleniti voluptatibus fugiat expedita officia recusandae veritatis alias unde aliquam minus excepturi. Vero deleniti repudiandae ab illum veniam, culpa alias at animi sint explicabo, eius ipsum expedita aperiam enim aut.</p>
  </div>

  <h2 class="section-title" style="top:214px">Experience</h2>
  <div class="section-body" style="top:217px">
    <article class="entry">
      <h3 class="entry-title">Web Company, Washington, U.S</h3>
      <p class="entry-dates">2012 - 2015</p>
      <p class="text">Lorem ipsum dolor sit amet, consectetur adipisicing elit inventore neque sint beatae cum explicabo laborum molestiae, rerum illum eaque deleniti voluptatibus sint explicabo, eius ipsum expedita aperiam enim aut.</p>
    </article>
    <article class="entry">
      <h3 class="entry-title">Web Design Limited, Northeastern U.S</h3>
      <p class="entry-dates">2015 - 2017</p>
      <p class="text">Lorem ipsum dolor sit amet, consectetur adipisicing elit inventore neque sint beatae cum explicabo laborum molestiae, rerum illum eaque deleniti voluptatibus sint explicabo, eius ipsum expedita aperiam enim aut.</p>
    </article>
    <article class="entry">
      <h3 class="entry-title">Pressline Private Company, Central Park, New York</h3>
      <p class="entry-dates">2018 - 2018</p>
      <ul class="entry-list">
        <li>Lorem ipsum dolor sit amet, consectetur adipisicing elit.</li>
        <li>Inventore neque sint beatae cum explicabo laborum molestiae,</li>
        <li>Lrerum illum eaque deleniti voluptatibus</li>
      </ul>
    </article>
  </div>

  <h2 class="section-label-plain" style="top:492px">Education</h2>
  <div class="section-body" style="top:505px">
    <article class="entry">
      <h3 class="entry-title">Bachelor of Comminucation, Hudson Valley University, New York</h3>
      <p class="entry-dates">August 2020 - Present</p>
      <ul class="entry-list tight"><li>Working towards a Communication Degree.</li></ul>
    </article>
    <article class="entry" style="margin-top:17px">
      <h3 class="entry-title">High School Diploma, Linden Grove High School, Linden Grove</h3>
      <p class="entry-dates">September 2015 - December 2019</p>
      <ul class="entry-list tight"><li>Graduated with High Honors</li></ul>
    </article>
  </div>

  <h2 class="section-title" style="top:638px">Skills</h2>
  <div class="section-body skills" style="top:642px">
    <div class="skill"><p class="skill-name">Html</p><div class="skill-bar"><div class="skill-level" style="width:90%"></div></div></div>
    <div class="skill"><p class="skill-name">Css</p><div class="skill-bar"><div class="skill-level" style="width:100%"></div></div></div>
    <div class="skill"><p class="skill-name">Javascript</p><div class="skill-bar"><div class="skill-level" style="width:96%"></div></div></div>
    <div class="skill"><p class="skill-name">Design</p><div class="skill-bar"><div class="skill-level" style="width:65%"></div></div></div>
    <div class="skill"><p class="skill-name">Php</p><div class="skill-bar"><div class="skill-level" style="width:75%"></div></div></div>
    <div class="skill"><p class="skill-name">Site Builder</p><div class="skill-bar"><div class="skill-level" style="width:100%"></div></div></div>
  </div>

  <h2 class="section-title" style="top:714px">Interest</h2>
  <div class="section-body" style="top:719px">
    <p class="interests"># Reading Book, # Surfing Internet, # Create New Design &amp; Web Resurach</p>
  </div>
</main>
</body>
</html>
```